R & T Summit Construction Business Card ideas

We want a business card to represents our company in a way that looks professional but is also a business card that is unique!

Industry/Entity Type

Construction Company

Contact Information for Business Card

open to all design ideas, just want to be able to see different options to choose from in either color or grayscale.

Requirements
Must have
• Our names and phone numbers
• Nolan Pritchett 512-804-2271
• Curtis Hale 512-693-1804
• Business logo

```html
<!DOCTYPE html>
<html lang="en">
<head>
<meta charset="utf-8">
<title>R &amp; T Summit Construction – Business Card</title>
<link rel="stylesheet" href="https://fonts.googleapis.com/css2?family=Montserrat:wght@300;400;500&display=swap">
<style>
  :root {
    --canvas: #e6e4e0;
    --card-light: #f4f4f3;
    --card-dark: #0b0b0b;
    --ink-dark: #1c1c1c;
    --ink-soft: #6c6c6c;
    --ink-light: #f2f2f2;
    --rule-dark: #2a2a2a;
    --rule-light: #cfcfcf;
  }
  * { box-sizing: border-box; margin: 0; padding: 0; }
  html, body {
    width: 1200px; height: 800px; overflow: hidden;
    background: var(--canvas);
    font-family: "Montserrat", Arial, sans-serif;
  }
  .stage {
    width: 1200px; height: 800px;
    display: flex; align-items: center; justify-content: center; gap: 48px;
  }
  .card {
    width: 532px; height: 304px;
    position: relative;
    box-shadow: 0 10px 28px rgba(0,0,0,0.22);
  }
  .card--front { background: var(--card-light); color: var(--ink-dark); }
  .card--back  { background: var(--card-dark); color: var(--ink-light); }

  .brand {
    display: flex; align-items: center; gap: 10px;
  }
  .brand__square {
    width: 14px; height: 14px; background: currentColor; flex: none;
  }
  .brand__name {
    font-weight: 500; font-size: 17px; letter-spacing: 0.06em;
    text-transform: uppercase; line-height: 1.25;
  }

  .card--front .brand {
    position: absolute; left: 34px; top: 132px; width: 230px;
  }
  .divider {
    position: absolute; left: 282px; top: 96px;
    width: 1px; height: 120px; background: var(--rule-dark);
  }
  .contact {
    position: absolute; left: 304px; top: 88px;
  }
  .contact__name {
    font-weight: 300; font-size: 22px; color: var(--ink-soft); line-height: 1.1;
  }
  .contact__title {
    font-weight: 500; font-size: 12px; color: var(--ink-soft); margin-bottom: 14px;
  }
  .contact__list { list-style: none; }
  .contact__item {
    display: flex; align-items: flex-start; gap: 9px;
    font-size: 11.5px; line-height: 1.35; margin-bottom: 6px; color: var(--ink-dark);
  }
  .contact__icon { width: 11px; height: 11px; flex: none; margin-top: 2px; fill: var(--ink-dark); }

  .card--back .brand {
    position: absolute; left: 50%; top: 50%;
    transform: translate(-50%, -50%);
  }
  .card--back .brand__name { font-size: 22px; white-space: nowrap; }
  .card--back .brand__rule {
    position: absolute; left: 24px; right: 0; bottom: -10px;
    height: 1px; background: var(--rule-light);
  }
</style>
</head>
<body>
<main class="stage">
  <section class="card card--front" aria-label="Card front">
    <div class="brand">
      <span class="brand__square"></span>
      <span class="brand__name">R &amp; T Summit Construction</span>
    </div>
    <div class="divider"></div>
    <div class="contact">
      <p class="contact__name">Your Name</p>
      <p class="contact__title">Job Title</p>
      <ul class="contact__list">
        <li class="contact__item">
          <svg class="contact__icon" viewBox="0 0 12 12"><path d="M6 0a4 4 0 0 0-4 4c0 3 4 8 4 8s4-5 4-8a4 4 0 0 0-4-4zm0 5.6A1.6 1.6 0 1 1 6 2.4a1.6 1.6 0 0 1 0 3.2z"/></svg>
          <span>00/00, Anywhere<br>Somewhere, ST-0000</span>
        </li>
        <li class="contact__item">
          <svg class="contact__icon" viewBox="0 0 12 12"><path d="M1 3.5C1 2 2.5 1 6 1s5 1 5 2.5V5H8.5V3.8h-5V5H1zM2.5 6h7L11 11H1z"/></svg>
          <span>000 000 0000</span>
        </li>
        <li class="contact__item">
          <svg class="contact__icon" viewBox="0 0 12 12"><path d="M0 2h12v1L6 7 0 3zm0 2.5 6 4 6-4V10H0z"/></svg>
          <span>Email@xyz.com</span>
        </li>
      </ul>
    </div>
  </section>

  <section class="card card--back" aria-label="Card back">
    <div class="brand">
      <span class="brand__square"></span>
      <span class="brand__name">R &amp; T Summit Construction</span>
      <span class="brand__rule"></span>
    </div>
  </section>
</main>
</body>
</html>
```